HIgh-end jewelry designer needs a business card design

I need a business card design for the ecclectic & rather expensive jewelry designs. My approach to my work is to combine very old jewelry offset with contemporary items. I enjoy the idea of legacy as well as repurposing finely crafted items that are not possible to create any longer. My desire is to celebrate the past in a contemporary & funky way. The name of my business is MERIVALE. I see my business card design as simple & yet enigmatic as possible. In the end... clean, simple & understated is the look I am after. Thank you for your consideration...

Target Market(s)

I will use this business card for the trade as well as customers

Industry/Entity Type

Business

Contact Information for Business Card

Corinne Halvard Owner/Designer 555-274-8163

Requirements
Must have
• Clean & simple sophisticated design using the word "Merivalle" as the logo. I like the idea of a play on the word itself, perhaps even using different fonts (i.e.: a bold helvetica combined with a lovely script). I'm afraid to say more because I don't want to limit creative input. Gosh, sometimes it's ok to break the rules!
Nice to have
• In my mind, I have imagined this business card to be simple, using my company name "Merivale" in a playful yet sophisticated manner. I believe that doing something beautifully simple can be a true challenge. I have imagined something with just black & white, however I am open to ideas... after all that's why I'm here!
Should not have
• As Mozart once said... "It has too many notes!" I know I'm being silly, but I don't want it to be complicated or overly ornate.

```html
<!DOCTYPE html>
<html lang="en">
<head>
<meta charset="utf-8">
<title>Merivale Business Card</title>
<link rel="stylesheet" href="https://fonts.googleapis.com/css2?family=Open+Sans:ital,wght@0,400;0,600;1,400&display=swap">
<style>
  :root {
    --backdrop: #cdbfa6;
    --card: #ffffff;
    --ornament-light: #f1f1f2;
    --ornament-mid: #dcdcde;
    --gold-dark: #a8782f;
    --gold: #c6964a;
    --ink: #1e1e1e;
    --divider: #d6d6d6;
  }
  * { box-sizing: border-box; margin: 0; padding: 0; }
  html, body {
    width: 1200px;
    height: 880px;
    overflow: hidden;
    background: var(--backdrop);
    font-family: "Open Sans", Arial, sans-serif;
  }
  .card {
    position: absolute;
    left: 100px;
    top: 155px;
    width: 1000px;
    height: 570px;
    background: var(--card);
    overflow: hidden;
  }
  .ornament-band {
    position: absolute;
    left: 0;
    top: 0;
    width: 1000px;
    height: 170px;
    background: linear-gradient(to bottom, var(--ornament-mid) 0%, var(--ornament-light) 60%, rgba(255,255,255,0) 100%);
  }
  .brand {
    position: absolute;
    left: 0;
    right: 0;
    top: 210px;
    text-align: center;
    padding-left: 90px;
  }
  .brand-name {
    display: inline-block;
    font-size: 66px;
    font-weight: 400;
    letter-spacing: 6px;
    text-transform: uppercase;
    color: var(--gold);
    line-height: 1;
  }
  .brand-rule {
    display: block;
    margin: 14px auto 0;
    width: 560px;
    height: 3px;
    background: var(--gold-dark);
  }
  .person {
    position: absolute;
    right: 440px;
    top: 375px;
    text-align: right;
    color: var(--ink);
  }
  .person-name {
    font-size: 40px;
    font-weight: 400;
    line-height: 1.2;
  }
  .person-name strong { font-weight: 600; }
  .person-role {
    font-size: 29px;
    font-style: italic;
    line-height: 1.3;
  }
  .divider {
    position: absolute;
    left: 590px;
    top: 355px;
    width: 2px;
    height: 150px;
    background: var(--divider);
  }
  .contact {
    position: absolute;
    left: 630px;
    top: 365px;
    list-style: none;
    color: var(--ink);
    font-size: 29px;
  }
  .contact-item {
    display: flex;
    align-items: center;
    gap: 18px;
    height: 54px;
  }
  .contact-icon { width: 22px; height: 22px; fill: var(--ink); }
</style>
</head>
<body>
  <div class="card">
    <div class="ornament-band" role="img" aria-label="Soft grey flourish ornament across the top of the card"></div>

    <div class="brand">
      <span class="brand-name">Merivalle</span>
      <span class="brand-rule"></span>
    </div>

    <div class="person">
      <p class="person-name">Corinne <strong>Halvard</strong></p>
      <p class="person-role">Owner/Designer</p>
    </div>

    <div class="divider"></div>

    <ul class="contact">
      <li class="contact-item">
        <svg class="contact-icon" viewBox="0 0 24 24" aria-hidden="true">
          <path d="M6.6 10.8a15.1 15.1 0 0 0 6.6 6.6l2.2-2.2a1 1 0 0 1 1-.25 11.4 11.4 0 0 0 3.6.57 1 1 0 0 1 1 1V20a1 1 0 0 1-1 1A17 17 0 0 1 3 4a1 1 0 0 1 1-1h3.5a1 1 0 0 1 1 1c0 1.25.2 2.45.57 3.57a1 1 0 0 1-.25 1z"/>
        </svg>
        <span>555-274-8163</span>
      </li>
      <li class="contact-item">
        <svg class="contact-icon" viewBox="0 0 24 24" aria-hidden="true">
          <path d="M3 6h18v12H3z M3 6l9 7 9-7" fill="none" stroke="#1e1e1e" stroke-width="2"/>
        </svg>
        <span>chalvard1@mail.com</span>
      </li>
    </ul>
  </div>
</body>
</html>
```